Web Design for online C2C site

We need a web design for a brand new website that has users logging into an account and uploading pictures of goods and services that they want to trade.
We like 'fresh' and simple websites that have a white background, with easy navigation, a splash of colour (grey, blue, and green is a colour scheme that appeals to us) but doesn't look overly boring.
The site needs a modern look for an old type of trade - a barter system.
We have attached a file with our logo and would like to use the top logo from the file (grey, green, and blue)
Updates
Project Deadline Extended
Reason: The timeline has been extended until this Sunday, December 2nd for all who require extra time to design a web layout.
Cheers,
Marisol
Industry/Entity Type
Trade
Look and feel
Each slider illustrates characteristics of the customer's brand and the style your logo design should communicate.

```html
<!DOCTYPE html>
<html lang="en">
<head>
<meta charset="utf-8">
<title>Barter Loop — Home</title>
<link href="https://fonts.googleapis.com/css2?family=Lato:ital,wght@0,400;0,700;1,400&family=Arimo:wght@400&display=swap" rel="stylesheet">
<style>
  :root {
    --page-bg: #f7f7f7;
    --page-bg-soft: #eeeeef;
    --text-dark: #2b2b2b;
    --text-body: #444444;
    --nav-text: #3a3a3a;
    --brand-blue: #5a5fb5;
    --brand-green: #47c01a;
    --green-top: #5ae21f;
    --green-bottom: #33b30b;
    --rule: #e2e2e2;
    --divider: #d6d6d6;
    --field-bg: #ececec;
    --field-border: #dadada;
    --box-bg: #fafafa;
    --photo-dark: #2a2a2e;
    --photo-light: #e9e9ea;
    --social-grey: #9aa3ad;
  }
  * { box-sizing: border-box; margin: 0; padding: 0; }
  html, body { width: 1200px; height: 960px; overflow: hidden; }
  body {
    position: relative;
    background: radial-gradient(ellipse at 50% 40%, #fcfcfc 0%, var(--page-bg) 55%, var(--page-bg-soft) 100%);
    font-family: "Lato", sans-serif;
    color: var(--text-dark);
  }

  .brand {
    position: absolute; left: 414px; top: 40px;
    display: flex; align-items: center; gap: 16px;
  }
  .brand-mark { width: 88px; height: 88px; border-radius: 50%; background: var(--brand-green); }
  .brand-name { font-family: "Lato", sans-serif; font-weight: 700; font-size: 48px; color: var(--brand-blue); letter-spacing: -0.5px; }

  .main-nav { position: absolute; top: 181px; left: 0; width: 1200px; height: 40px; }
  .nav-item {
    position: absolute; top: 0; height: 40px; line-height: 40px;
    font-size: 19px; color: var(--nav-text); text-decoration: none; transform: translateX(-50%);
  }
  .nav-item.is-active {
    left: 331px; width: 96px; text-align: center; color: #fff;
    background: linear-gradient(var(--green-top), var(--green-bottom));
    border: 1px solid #2f9a0e;
  }
  .nav-sep { position: absolute; top: 7px; width: 1px; height: 30px; background: var(--divider); }

  .rule { position: absolute; left: 48px; width: 1104px; height: 1px; background: var(--rule); }

  .hero-photo {
    position: absolute; left: 108px; top: 294px; width: 510px; height: 384px;
    background: linear-gradient(100deg, var(--photo-light) 0%, #cfcfd2 30%, var(--photo-dark) 55%, #8c8c90 75%, var(--photo-light) 100%);
  }

  .login-box {
    position: absolute; left: 700px; top: 322px; width: 386px; height: 271px;
    background: var(--box-bg); border: 1px solid #e6e6e6; border-radius: 18px;
    box-shadow: 0 1px 4px rgba(0,0,0,0.06);
  }
  .login-title { position: absolute; left: 44px; top: 16px; font-size: 22px; font-weight: 700; color: var(--brand-blue); }
  .login-title .accent { color: var(--brand-green); }
  .login-divider { position: absolute; left: 16px; right: 16px; top: 55px; height: 1px; background: var(--rule); }
  .field {
    position: absolute; left: 37px; width: 313px; height: 45px;
    background: var(--field-bg); border: 2px solid var(--field-border); border-radius: 4px;
    padding-left: 10px; line-height: 41px; font-size: 20px; font-style: italic; color: #777;
  }
  .field-name { top: 79px; }
  .field-pass { top: 140px; font-style: normal; font-size: 15px; letter-spacing: 2px; }
  .forgot { position: absolute; left: 42px; top: 211px; font-size: 13px; font-style: italic; color: var(--text-dark); }
  .login-btn {
    position: absolute; left: 266px; top: 202px; width: 82px; height: 34px;
    border: 1px solid #d8d8d8; border-radius: 6px; background: linear-gradient(#ffffff, #e8e8e8);
    font-family: "Lato", sans-serif; font-weight: 700; font-style: italic; font-size: 16px; color: var(--brand-blue);
  }

  .footer-col { position: absolute; top: 754px; }
  .footer-col h3 { font-family: "Lato", sans-serif; font-weight: 700; font-size: 16px; color: var(--text-dark); margin-bottom: 11px; }
  .footer-col li { list-style: none; font-family: "Arimo", sans-serif; font-size: 13px; line-height: 21.6px; color: var(--text-body); }
  .footer-sep { position: absolute; top: 752px; width: 1px; height: 146px; background: var(--divider); }
  .social { display: flex; gap: 8px; margin-top: 2px; }
  .social span { width: 19px; height: 19px; background: var(--social-grey); border-radius: 2px; }

  .copyright {
    position: absolute; top: 917px; left: 0; width: 1260px; text-align: center;
    font-family: "Arimo", sans-serif; font-size: 13px; color: var(--text-body);
  }
</style>
</head>
<body>
  <header>
    <div class="brand">
      <span class="brand-mark"></span>
      <span class="brand-name">Barter Loop</span>
    </div>
    <nav class="main-nav">
      <a class="nav-item is-active" href="#">Home</a>
      <span class="nav-sep" style="left:394px"></span>
      <a class="nav-item" href="#" style="left:463px">About</a>
      <span class="nav-sep" style="left:534px"></span>
      <a class="nav-item" href="#" style="left:608px">Browse</a>
      <span class="nav-sep" style="left:682px"></span>
      <a class="nav-item" href="#" style="left:758px">Services</a>
      <span class="nav-sep" style="left:835px"></span>
      <a class="nav-item" href="#" style="left:911px">Contact</a>
    </nav>
  </header>

  <div class="rule" style="top:240px"></div>

  <main>
    <div class="hero-photo" role="img" aria-label="Woman at a desk receiving shopping bags handed out through a computer monitor"></div>

    <section class="login-box">
      <h2 class="login-title">Member’s <span class="accent">Login Area</span></h2>
      <div class="login-divider"></div>
      <div class="field field-name">Login Name</div>
      <div class="field field-pass">********</div>
      <span class="forgot">Forget your Username/ Password</span>
      <button class="login-btn">Login</button>
    </section>
  </main>

  <div class="rule" style="top:678px"></div>

  <footer>
    <div class="footer-col" style="left:108px">
      <h3>Who We Are</h3>
      <ul><li>About Us</li><li>Sitemap</li><li>Website Terms</li><li>Terms of Business</li><li>Privacy Policy</li></ul>
    </div>
    <span class="footer-sep" style="left:262px"></span>
    <div class="footer-col" style="left:329px">
      <h3>Community</h3>
      <ul><li>Business Websites</li><li>Reviews</li><li>Quick Tour</li><li>Pricing</li><li>Free Trial</li></ul>
    </div>
    <span class="footer-sep" style="left:491px"></span>
    <div class="footer-col" style="left:550px">
      <h3>Event</h3>
      <ul><li>Marketing Tips</li><li>Search Optimisation</li><li>Social Media</li><li>Video Marketing</li><li>Business Cases</li></ul>
    </div>
    <span class="footer-sep" style="left:739px"></span>
    <div class="footer-col" style="left:787px">
      <h3>Services</h3>
      <ul><li>Help/Contact us</li><li>Business directory</li><li>Legal notices</li><li>Privacy policy</li><li>Terms &amp; Conditions</li></ul>
    </div>
    <span class="footer-sep" style="left:956px"></span>
    <div class="footer-col" style="left:995px">
      <h3>Follow us</h3>
      <div class="social"><span></span><span></span><span></span><span></span></div>
    </div>
    <p class="copyright">Copyright © 2012 Barter Loop Company. All rights reserved.</p>
  </footer>
</body>
</html>
```